A4 Menu needed for cafe - attached design

Need an A4 menu designed for our cafe.
I have attached our catering menu - I would like the new menu to be designed in the exact same way.

I have attached the text that needs to appear on the menu

Industry/Entity Type

Catering

```html
<!DOCTYPE html>
<html lang="en">
<head>
<meta charset="utf-8">
<title>Ward Round Canteen – Catering Menu</title>
<link rel="stylesheet" href="https://fonts.googleapis.com/css2?family=Cinzel:wght@400;500&family=Dancing+Script:wght@500&family=Open+Sans:ital@1&family=Crimson+Text&display=swap">
<style>
  :root {
    --page: #2a0e22;
    --page-deep: #230b1c;
    --gap: #ffffff;
    --panel: rgba(62, 58, 84, 0.45);
    --tab: #8d835a;
    --tab-light: #9c9267;
    --tab-ink: #2a1c1c;
    --gold: #f2e467;
    --cream: #f4efe2;
    --item: #efeae0;
    --price: #e7d36a;
  }
  html, body { margin: 0; padding: 0; overflow: hidden; }
  body { width: 841px; height: 1200px; background: var(--gap); position: relative; }
  .page {
    position: absolute; left: 0; width: 841px;
    background: radial-gradient(circle at 50% 40%, var(--page) 0%, var(--page-deep) 100%);
  }
  .page--front { top: 0; height: 593px; }
  .page--back { top: 604px; height: 596px; }

  .brand {
    position: absolute; left: 351px; top: 39px; width: 140px; height: 137px;
    display: flex; flex-direction: column; align-items: center; justify-content: center; gap: 12px;
  }
  .brand__mark { width: 18px; height: 18px; border-radius: 50%; background: var(--gold); }
  .brand__name {
    font-family: "Cinzel", serif; font-size: 17px; line-height: 1.2; color: var(--gold);
    text-align: center; letter-spacing: 1px;
  }
  .menu-title {
    position: absolute; left: 0; width: 841px; top: 188px; margin: 0; text-align: center;
    font-family: "Cinzel", serif; font-weight: 500; font-size: 29px; color: var(--gold);
    letter-spacing: 1px;
  }

  .section { position: absolute; }
  .section__panel { position: absolute; background: var(--panel); border-radius: 14px; }
  .section__tab {
    position: absolute; margin: 0; display: flex; align-items: center; justify-content: center;
    background: linear-gradient(var(--tab-light), var(--tab)); border-radius: 9px;
    font-family: "Cinzel", serif; font-weight: 400; font-size: 25px; color: var(--tab-ink);
    letter-spacing: 1px;
  }
  .items {
    position: absolute; margin: 0; padding: 0; list-style: none;
    font-family: "Dancing Script", cursive; font-weight: 500; font-size: 17px; line-height: 20px;
  }
  .items li { position: relative; color: var(--item); white-space: nowrap; }
  .items .price { position: absolute; top: 0; color: var(--price); }

  .note {
    position: absolute; left: 0; width: 841px; top: 557px; margin: 0; text-align: center;
    font-family: "Open Sans", sans-serif; font-style: italic; font-size: 11.5px; color: var(--gold);
  }
  .contact {
    position: absolute; left: 0; width: 841px; margin: 0; text-align: center;
    font-family: "Crimson Text", serif; font-size: 11.5px; color: var(--cream);
  }
  .page--front .contact { top: 578px; }
  .page--back .contact { top: 580px; }
</style>
</head>
<body>

<section class="page page--front">
  <div class="brand">
    <span class="brand__mark"></span>
    <span class="brand__name">Ward Round<br>Canteen</span>
  </div>
  <h1 class="menu-title">CATERING MENU</h1>

  <div class="section section--breakfast">
    <div class="section__panel" style="left:29px; top:272px; width:366px; height:277px;"></div>
    <h2 class="section__tab" style="left:71px; top:237px; width:282px; height:56px;">BREAKFAST</h2>
    <ul class="items" style="left:61px; top:303px; width:330px;">
      <li>Toast<span class="price" style="left:232px;">$2 per slice</span></li>
      <li>Raisin Toast<span class="price" style="left:232px;">$2 per slice</span></li>
      <li>Egg Bacon and Cheese Roll<span class="price" style="left:232px;">$6.5</span></li>
      <li>Veggie Brekky Wrap<span class="price" style="left:232px;">$6.5</span></li>
      <li>Ham and Cheese French Toast<span class="price" style="left:232px;">$6.5</span></li>
      <li>Ham and Cheese Toastie<span class="price" style="left:232px;">$5.5</span></li>
      <li>Cheese and Tomato Toastie<span class="price" style="left:232px;">$5.5</span></li>
      <li>Ham and Cheese Croissant<span class="price" style="left:232px;">$6.5</span></li>
      <li>Cheese and tomato Croissant<span class="price" style="left:232px;">$6.0</span></li>
      <li>Ham Cheese and Tomato Toastie<span class="price" style="left:232px;">$6.0</span></li>
      <li>Plain Croissant<span class="price" style="left:232px;">$3.5</span></li>
    </ul>
  </div>

  <div class="section section--light">
    <div class="section__panel" style="left:441px; top:272px; width:370px; height:277px;"></div>
    <h2 class="section__tab" style="left:484px; top:237px; width:283px; height:56px;">SOMETHING LIGHT</h2>
    <ul class="items" style="left:476px; top:311px; width:320px;">
      <li>Mixed Yoghurts<span class="price" style="left:236px;">$5.5</span></li>
      <li>Granola and Fruit Yoghurt<span class="price" style="left:236px;">$5.5</span></li>
      <li>Chia Pudding<span class="price" style="left:236px;">$5.5</span></li>
      <li>Bircher Muesli<span class="price" style="left:236px;">$5.5</span></li>
      <li>Fruit Salad<span class="price" style="left:236px;">$5.5</span></li>
      <li>Banana Bread<span class="price" style="left:236px;">$4.5</span></li>
      <li>Muffins – made fresh daily<span class="price" style="left:236px;">$4.5</span></li>
      <li>Slices<span class="price" style="left:236px;">$4.0</span></li>
      <li>Cookies<span class="price" style="left:236px;">$4.0</span></li>
      <li>Choc Crunch Energy Bite<span class="price" style="left:236px;">$4.0</span></li>
    </ul>
  </div>

  <p class="note">Cups/Plates/Serviettes can be provided at a charge of $1 per person</p>
  <p class="contact">visit us instore to discuss catering options, or call 0400 123 456 or email us hello@wardroundcanteen.com</p>
</section>

<section class="page page--back">
  <div class="section section--lunch">
    <div class="section__panel" style="left:237px; top:160px; width:367px; height:280px;"></div>
    <h2 class="section__tab" style="left:280px; top:127px; width:281px; height:56px;">LUNCH</h2>
    <ul class="items" style="left:269px; top:200px; width:320px;">
      <li>Pre made Sandwiches<span class="price" style="left:236px;">$6.5/$7.5</span></li>
      <li>Pre made Focaccias<span class="price" style="left:236px;">$8.5</span></li>
      <li>Pre made Wraps<span class="price" style="left:236px;">$7.5</span></li>
      <li>Pre made Mini Rolls<span class="price" style="left:236px;">$4.0</span></li>
      <li>Pre made Baguettes<span class="price" style="left:236px;">$9.0</span></li>
      <li>Pre made Bagels<span class="price" style="left:236px;">$9.0</span></li>
      <li>Fresh Salads made daily<span class="price" style="left:236px;">$9.5</span></li>
      <li>Hot Chips<span class="price" style="left:236px;">$4.5</span></li>
      <li>Plain Hamburger<span class="price" style="left:236px;">$7.5</span></li>
      <li>Hamburger with the Lot<span class="price" style="left:236px;">$9.0</span></li>
      <li>Chicken Schnitzel Burger<span class="price" style="left:236px;">$8.5</span></li>
    </ul>
  </div>

  <p class="contact">visit us instore to discuss catering options, or call 0400 123 456 or email us hello@wardroundcanteen.com</p>
</section>

</body>
</html>
```